Tallowreed Advisory Partners Business Card Design

We have the logo we just need someone to design a modern business card design.

Name: Desmond Munkalt
Phone: 3055550148
Mobile: 9175550193
Web:www.tallowreedadvisory.example
email: dmunkalt@tallowreedadvisory.example
Company: Tallowreed Advisory Partners
Title: CEO

Address: 718 Quillmore Ave, Miami, Florida 33190

Target Market(s)

companies over 100 employees

Industry/Entity Type

Business

```html
<!DOCTYPE html>
<html lang="en">
<head>
<meta charset="utf-8">
<title>Tallowreed Advisory Partners — Business Card</title>
<link rel="stylesheet" href="https://fonts.googleapis.com/css2?family=Inter:wght@300;400;700&display=swap">
<style>
  :root {
    --backdrop: #e6e4e1;
    --card-dark: #0b0b0c;
    --card-light: #efefef;
    --brand-blue: #1a5ee6;
    --ink: #2b2b2b;
    --ink-soft: #3a3a3a;
    --paper-white: #f4f4f4;
  }
  * { box-sizing: border-box; margin: 0; padding: 0; }
  html, body {
    width: 1200px;
    height: 900px;
    overflow: hidden;
    background: var(--backdrop);
    font-family: "Inter", Arial, sans-serif;
  }
  .card-set {
    position: relative;
    width: 1200px;
    height: 900px;
  }
  .card {
    position: absolute;
    top: 152px;
    width: 340px;
    height: 595px;
    box-shadow: 0 6px 18px rgba(0,0,0,0.18);
  }

  /* Front side */
  .card-front {
    left: 195px;
    background: var(--card-dark);
    color: var(--paper-white);
  }
  .front-brand {
    position: absolute;
    top: 118px;
    left: 0;
    width: 100%;
    text-align: center;
  }
  .brand-dot {
    display: block;
    width: 86px;
    height: 86px;
    margin: 0 auto 22px;
    border-radius: 50%;
    background: var(--brand-blue);
  }
  .brand-name {
    font-weight: 700;
    font-size: 17px;
    letter-spacing: 0.06em;
    line-height: 1.35;
    text-transform: uppercase;
    color: var(--paper-white);
  }
  .front-rule {
    position: absolute;
    left: 96px;
    right: 34px;
    top: 506px;
    height: 2px;
    background: var(--brand-blue);
  }
  .front-web {
    position: absolute;
    right: 34px;
    top: 522px;
    font-size: 14px;
    color: var(--paper-white);
  }
  .front-web strong { font-weight: 700; }

  /* Back side */
  .card-back {
    left: 665px;
    background: var(--card-light);
    color: var(--ink);
  }
  .back-dot {
    position: absolute;
    top: 58px;
    left: 40px;
    width: 128px;
    height: 128px;
    border-radius: 50%;
    background: var(--brand-blue);
  }
  .person {
    position: absolute;
    top: 248px;
    left: 52px;
    font-weight: 300;
    font-size: 21px;
    line-height: 1.2;
    color: var(--ink);
  }
  .back-rule {
    position: absolute;
    left: 52px;
    right: 0;
    top: 318px;
    height: 2px;
    background: var(--brand-blue);
  }
  .contact {
    position: absolute;
    top: 338px;
    left: 52px;
    font-weight: 300;
    font-size: 14.5px;
    line-height: 1.3;
    color: var(--ink-soft);
  }
  .phone-line { display: flex; gap: 10px; }
  .phone-label { color: var(--brand-blue); width: 12px; }
  .contact-email { margin-top: 18px; }
  .contact-address { margin-top: 18px; }
  .contact-web { margin-top: 20px; font-weight: 400; }
  .contact-web strong { font-weight: 700; }
</style>
</head>
<body>
<main class="card-set">
  <section class="card card-front" aria-label="Business card front">
    <div class="front-brand">
      <span class="brand-dot"></span>
      <p class="brand-name">Tallowreed<br>Advisory Partners</p>
    </div>
    <div class="front-rule"></div>
    <p class="front-web">www.<strong>tallowreed</strong>advisory.example</p>
  </section>

  <section class="card card-back" aria-label="Business card back">
    <span class="back-dot"></span>
    <div class="person">
      <p class="person-name">Desmond Munkalt</p>
      <p class="person-title">CEO</p>
    </div>
    <div class="back-rule"></div>
    <div class="contact">
      <p class="phone-line"><span class="phone-label">T</span><span>3055550148</span></p>
      <p class="phone-line"><span class="phone-label">M</span><span>9175550193</span></p>
      <p class="contact-email">dmunkalt@tallowreedadvisory.example</p>
      <p class="contact-address">718 Quillmore Ave, Miami<br>Florida 33190</p>
      <p class="contact-web">www.<strong>tallowreed</strong>advisory.example</p>
    </div>
  </section>
</main>
</body>
</html>
```